Business Card Design To Look Just Like a Credit Card- Needed

I would like to take my new Logo just designed here at Pixel Harbor and make a new business card and template for future additional sales people.
The credit card should have an eye catching design but look real. I have seen some that have similar logos to LORU or TrustPlaque too. However,it must have a smart chip design in it too. Make sure it has a black fake magnetic strip and other characteristics of an actual modern credit card.
This may be printed on paper and blank plastic cards.

Most the information will be on the back but the name will be on front with the logo, phone number.

Must Have Info:
Leonard Whitfield
President

2964 Maple Hollow Rd, Bldg 417
Linden Falls, VT 05123
319-555-0187
leonard@brightledgerco.net
Updates

Phone number is 585 area code not 252! my bad

also, please add website address www.brightledgerco.net
Thanks,

LW

Industry/Entity Type

Credit Card

Requirements
Must have
• My Logo, smart chip, fake magnetic strip

```html
<!DOCTYPE html>
<html lang="en">
<head>
<meta charset="utf-8">
<title>Bright Ledger – Business Card</title>
<link rel="stylesheet" href="https://fonts.googleapis.com/css2?family=Exo+2:wght@500;600;800&display=swap">
<style>
  :root{
    --stage:#e9e9ee;
    --card-light:#ffffff;
    --card-shade:#e6e8e4;
    --green:#17792b;
    --lime:#8cbd1e;
    --ink:#3a3a3a;
    --stripe:#111111;
    --gold-light:#e8c467;
    --gold-dark:#b88a2a;
    --gold-line:#a57a22;
    --tile:#c9cbc9;
  }
  *{margin:0;padding:0;box-sizing:border-box}
  html,body{width:1200px;height:987px;overflow:hidden}
  body{background:var(--stage);font-family:"Exo 2",sans-serif;position:relative}

  .card{
    position:absolute;width:540px;height:340px;border-radius:26px;overflow:hidden;
    background:radial-gradient(ellipse at 60% 55%,var(--card-light) 0%,var(--card-shade) 100%);
    box-shadow:0 10px 30px rgba(0,0,0,.18);
  }
  .card--front{left:60px;top:560px}
  .card--back{left:600px;top:90px}

  .sunburst{position:absolute;inset:0;
    background:radial-gradient(circle at 65% 60%,rgba(255,255,255,.9) 0%,rgba(255,255,255,0) 70%)}

  .brand{position:absolute;display:flex;align-items:center;gap:12px}
  .brand__mark{width:34px;height:34px;background:var(--green);border-radius:4px}
  .brand__name{font-weight:800;color:var(--green);font-size:38px;line-height:1;letter-spacing:1px;text-transform:uppercase}
  .card--front .brand{left:34px;top:38px}
  .card--back .brand{left:130px;top:118px}

  .mag-stripe{position:absolute;left:0;right:0;top:34px;height:52px;background:var(--stripe)}

  .chip-tile{position:absolute;left:430px;top:150px;width:64px;height:64px;border-radius:12px;
    background:linear-gradient(135deg,#e4e5e4,var(--tile))}
  .chip{position:absolute;left:424px;top:226px}

  .holder{position:absolute;right:150px;top:160px;text-align:right}
  .holder__name{font-weight:600;font-size:26px;color:var(--green);line-height:1.1}
  .holder__title{font-weight:600;font-size:20px;color:var(--lime)}

  .phone{position:absolute;left:34px;top:268px;font-weight:600;font-size:46px;color:var(--green);letter-spacing:5px}

  .contact{position:absolute;left:60px;top:196px;list-style:none;font-size:17px;color:var(--ink);font-weight:500}
  .contact li{display:flex;align-items:center;gap:8px;margin-bottom:8px}
  .contact svg{flex:none}
</style>
</head>
<body>

<section class="card card--back" aria-label="Card back">
  <div class="sunburst" role="img" aria-label="Soft light ray background"></div>
  <div class="mag-stripe"></div>
  <div class="brand">
    <span class="brand__mark"></span>
    <span class="brand__name">Bright Ledger</span>
  </div>
  <ul class="contact">
    <li>
      <svg width="16" height="16" viewBox="0 0 16 16"><rect x="1" y="3" width="14" height="10" rx="2" fill="var(--lime)"/><path d="M1.5 4 8 9l6.5-5" stroke="#fff" stroke-width="1.4" fill="none"/></svg>
      sales@brightledgerco.net
    </li>
    <li>
      <svg width="16" height="16" viewBox="0 0 16 16"><path d="M8 1 1 7h2v7h4v-4h2v4h4V7h2z" fill="var(--lime)"/></svg>
      2964 Maple Hollow Rd, Bldg 417, Linden Falls, VT 05123
    </li>
  </ul>
</section>

<section class="card card--front" aria-label="Card front">
  <div class="sunburst" role="img" aria-label="Soft light ray background"></div>
  <div class="brand">
    <span class="brand__mark"></span>
    <span class="brand__name">Bright Ledger</span>
  </div>
  <div class="chip-tile"></div>
  <svg class="chip" width="76" height="60" viewBox="0 0 76 60" aria-label="Smart chip">
    <defs>
      <linearGradient id="gold" x1="0" y1="0" x2="1" y2="1">
        <stop offset="0" stop-color="var(--gold-light)"/>
        <stop offset="1" stop-color="var(--gold-dark)"/>
      </linearGradient>
    </defs>
    <rect x="1" y="1" width="74" height="58" rx="10" fill="url(#gold)" stroke="var(--gold-line)"/>
    <g stroke="var(--gold-line)" stroke-width="1.5" fill="none">
      <rect x="26" y="18" width="24" height="24" rx="4"/>
      <path d="M1 20h25M1 40h25M50 20h25M50 40h25M38 1v17M38 42v17"/>
    </g>
  </svg>
  <div class="holder">
    <p class="holder__name">Leonard Whitfield</p>
    <p class="holder__title">President</p>
  </div>
  <p class="phone">319-555-0187</p>
</section>

</body>
</html>
```